Need UI Design for HRIS/Company Employee Portal

Currently have a custom built system that we hire and use as our employee database and employee portal for everyone in our company. The software has evolved dramatically and needs to be completely user friendly and aesthetically pleasing. Attached are a few ideas and pages we already have. Please make 5 designs for the 5 different pages below. Would need all specifications of content used, color code, font/typography, icons used, etc. We can pretty much pull any information from anywhere we have for example, employee photo, address, DOB, Hire date, Title, ETC.

-Company Staff/Admin Welcome Page
- We want quick shortcuts/buttons or icons for staff functions, such as terminate, hire, information change, reports, etc
-Employee Profile Welcome Page
- We want quick shortcuts/buttons or icons for direct deposit, time off request, information change, pay stubs
-List of Applications/Candidates Page
-Profile Search Page
-Manage Inventory

Target Market(s)

Employees

Industry/Entity Type

It Company

Coding

Coded - Design and coding required

Number of Pages Required

5+ page

Font styles to use
Sans Serif

Requirements
Must have
• Must be professional! Aesthetics, Icons, Easy User Interface, Modern New technology look, can be responsive to mobile
Should not have
• Nothing old school

```html
<!DOCTYPE html>
<html lang="en">
<head>
<meta charset="utf-8">
<title>Employee Profile</title>
<link href="https://fonts.googleapis.com/css2?family=Open+Sans:ital,wght@0,400;0,600;0,700;1,400&display=swap" rel="stylesheet">
<style>
:root{
  --page:#f5f7fa;
  --card:#ffffff;
  --line:#e1e5eb;
  --blue:#2b63a6;
  --blue-light:#3876bb;
  --blue-dark:#1c4c8c;
  --yellow:#ecc51c;
  --yellow-dark:#e2b610;
  --text:#4a4a4a;
  --muted:#666;
  --stripe:#f1f4f8;
  --footer:#1c1c1c;
}
*{box-sizing:border-box;margin:0;padding:0}
html,body{width:1200px;height:980px;overflow:hidden}
body{background:var(--page);font-family:"Open Sans",Arial,sans-serif;color:var(--text);position:relative}
.wrap{position:absolute;left:99px;width:1002px}
.header{top:0;height:120px}
.brand{position:absolute;left:34px;top:46px;display:flex;align-items:center;gap:10px}
.brand-dot{width:30px;height:30px;border-radius:50%;background:var(--blue)}
.brand-name{font-size:15px;font-weight:700;color:var(--blue);letter-spacing:.3px}
.contact-btn{position:absolute;right:0;top:45px;width:140px;height:40px;background:linear-gradient(var(--yellow),var(--yellow-dark));color:#fff;font-size:12px;display:flex;align-items:center;justify-content:center;border-radius:2px}
.nav{top:127px;height:50px;background:linear-gradient(var(--blue-light),var(--blue-dark));display:flex;align-items:center}
.nav a{color:#fff;text-decoration:none;font-size:11.5px;height:100%;display:flex;align-items:center}
.nav a.active{background:linear-gradient(var(--yellow),var(--yellow-dark));padding:0 31px;margin-right:26px}
.nav a+a{margin-right:0}
.nav .items{display:flex;flex:1;justify-content:space-between;padding-right:36px}
.card{position:absolute;background:var(--card);border:1px solid var(--line)}
.profile{left:99px;top:203px;width:319px;height:357px;text-align:center}
.photo{width:135px;height:135px;border-radius:50%;margin:22px auto 0;border:4px solid #e6e6e6;background:radial-gradient(circle at 50% 40%,#8a6a58,#4b3b35 70%)}
.profile h2{font-weight:400;font-size:13px;color:var(--blue);margin-top:20px}
.profile p{font-size:11px;line-height:23px;color:var(--muted);padding:4px 26px 0}
.hire{font-size:12px;color:var(--blue);margin-top:13px}
.years{display:inline-block;font-size:12px;color:var(--blue);text-decoration:underline;margin-top:11px}
.info{left:441px;top:203px;width:660px;height:357px;padding-top:1px}
.row{height:50px;display:flex;align-items:center;padding-left:28px;font-size:12px}
.row:nth-child(even){background:var(--stripe)}
.row svg{width:26px;height:26px;flex:none}
.row .label{width:90px;margin-left:10px;color:#444}
.row .value{color:var(--muted)}
.permits{left:99px;top:586px;width:319px;height:259px;padding:20px}
.permit-box{background:#f3f5f8;height:220px;border-bottom:3px solid #d5e1ec;text-align:center;padding-top:22px;font-size:11.5px;color:#444}
.permit-box h3{font-weight:400;font-size:14px;margin-bottom:9px}
.permit-box div{line-height:26px}
.permit-box h3.second{margin-top:10px;margin-bottom:0}
.permit-box .lic{line-height:17px}
.message{position:absolute;left:440px;width:319px;height:120px;color:#fff;text-align:center;padding-top:24px}
.message h3{font-weight:400;font-size:14px;letter-spacing:.2px}
.message p{font-style:italic;font-size:11px;line-height:20px;margin-top:8px;position:relative}
.message .q{font-style:normal;font-size:22px;font-weight:700;opacity:.55;vertical-align:-6px}
.msg-employee{top:586px;background:var(--blue);border-bottom:3px solid #a8b9cf}
.msg-company{top:728px;background:#eac51e;border-bottom:3px solid #a9afb9}
.calendar{left:782px;top:586px;width:319px;height:259px}
.cal{position:absolute;left:25px;top:25px;width:268px;height:205px;border:1px solid var(--line)}
.cal-head{height:33px;background:#f3f5f8;display:flex;align-items:center;justify-content:space-between}
.cal-head span{font-size:11px;color:var(--blue)}
.cal-btn{width:19px;height:33px;background:var(--blue);display:flex;align-items:center;justify-content:center}
.cal-days{display:grid;grid-template-columns:repeat(7,33.3px);margin:14px 0 0 16px;font-size:7px;font-weight:700;color:#333;text-align:center}
.cal-grid{display:grid;grid-template-columns:repeat(7,33.3px);margin:7px 0 0 16px;border-top:1px solid var(--line);border-left:1px solid var(--line)}
.cal-grid span{height:25px;border-right:1px solid var(--line);border-bottom:1px solid var(--line);font-size:7.5px;display:flex;align-items:center;justify-content:center;color:#555}
.cal-grid span.out{color:#ccc}
.cal-grid span.today{background:var(--yellow);color:#fff;outline:1px solid #b79a10}
.footer{position:absolute;left:0;top:891px;width:1200px;height:89px;background:var(--footer);color:#bbb}
.foot-links{position:absolute;left:98px;top:21px;font-size:9.5px;display:flex;gap:9px}
.foot-links i{font-style:normal;color:#888}
.copy{position:absolute;left:98px;top:52px;font-size:9.5px}
.social{position:absolute;left:843px;top:38px;display:flex;align-items:center;gap:18px;font-size:9.5px}
.social b{display:block;width:11px;height:11px;border-radius:50%;background:#777}
</style>
</head>
<body>
<header class="wrap header">
  <div class="brand"><span class="brand-dot"></span><span class="brand-name">NORTHGATE PATROL SERVICES, INC.</span></div>
  <a class="contact-btn">CONTACT US</a>
</header>

<nav class="wrap nav">
  <a class="active">HOME</a>
  <div class="items">
    <a>PERSONAL LICENSES</a><a>FORMS/REQUESTS</a><a>TEAM CONTACT</a><a>BENEFITS</a><a>TRAINING</a><a>EQUIPMENT</a><a>HELP</a>
  </div>
</nav>

<section class="card profile">
  <div class="photo" role="img" aria-label="Employee portrait photo"></div>
  <h2>-Daniel Marlowe</h2>
  <p>Sed ut perspiciatis unde omnis iste natus error sit laudantium, totam rem aperiam, eaque ipsa quae ab illo inventore veritatis et quasi...</p>
  <div class="hire">
    <svg width="11" height="11" viewBox="0 0 12 12" style="vertical-align:-1px"><rect x="1" y="2" width="10" height="9" fill="none" stroke="#2b63a6" stroke-width="1.3"/><path d="M1 5h10M4 1v2M8 1v2M4 7h1M7 7h1M4 9h1M7 9h1" stroke="#2b63a6" stroke-width="1.2"/></svg>
    Hire Date : 22 / 08 / 2016</div>
  <a class="years">17 Years</a>
</section>

<section class="card info">
  <div class="row"><svg viewBox="0 0 26 26"><circle cx="13" cy="13" r="12" fill="none" stroke="#2b63a6" stroke-width="1.5"/><circle cx="13" cy="10.5" r="2.6" fill="#2b63a6"/><path d="M8.5 17.5a4.5 4.2 0 0 1 9 0z" fill="#2b63a6"/></svg><span class="label">NAME</span><span class="value">: Daniel Marlowe</span></div>
  <div class="row"><svg viewBox="0 0 26 26"><circle cx="13" cy="13" r="12" fill="none" stroke="#2b63a6" stroke-width="1.5"/><path d="M13 19s-4-4.5-4-7.5a4 4 0 0 1 8 0c0 3-4 7.5-4 7.5z" fill="#2b63a6"/><circle cx="13" cy="11.5" r="1.5" fill="#fff"/></svg><span class="label">ADDRESS</span><span class="value">: 48 Harbor Works, Linden Street, Riverton-55130</span></div>
  <div class="row"><svg viewBox="0 0 26 26"><circle cx="13" cy="13" r="12" fill="none" stroke="#2b63a6" stroke-width="1.5"/><path d="M8 9l3-1.2 4 1.2 3-1.2v9l-3 1.2-4-1.2-3 1.2z" fill="#2b63a6"/></svg><span class="label">CITY</span><span class="value">: United States America For Riverton</span></div>
  <div class="row"><svg viewBox="0 0 26 26"><circle cx="13" cy="13" r="12" fill="none" stroke="#2b63a6" stroke-width="1.5"/><path d="M7.5 13.5 18 8.5l-3 10-2.5-3.5z" fill="#2b63a6"/></svg><span class="label">ZIP</span><span class="value">: Zip code *********55130</span></div>
  <div class="row"><svg viewBox="0 0 26 26"><circle cx="13" cy="13" r="12" fill="none" stroke="#2b63a6" stroke-width="1.5"/><path d="M9.5 8.5l2 -0.5 1 2.5-1.2 1a6 6 0 0 0 3 3l1-1.2 2.5 1-.5 2c-4 .5-8.5-4-7.8-7.8z" fill="#2b63a6"/></svg><span class="label">PHONE</span><span class="value">: (000) 2222-4444-7777</span></div>
  <div class="row"><svg viewBox="0 0 26 26"><circle cx="13" cy="13" r="12" fill="none" stroke="#2b63a6" stroke-width="1.5"/><rect x="10" y="7.5" width="6" height="11" rx="1" fill="none" stroke="#2b63a6" stroke-width="1.5"/><circle cx="13" cy="16.3" r=".8" fill="#2b63a6"/></svg><span class="label">CELL PHONE</span><span class="value">: +111-5555-3030</span></div>
  <div class="row"><svg viewBox="0 0 26 26"><circle cx="13" cy="13" r="12" fill="none" stroke="#2b63a6" stroke-width="1.5"/><rect x="8" y="9" width="10" height="8" fill="none" stroke="#2b63a6" stroke-width="1.4"/><path d="M8 9.5l5 4 5-4" fill="none" stroke="#2b63a6" stroke-width="1.4"/></svg><span class="label">E-MAIL</span><span class="value">: info@northgatepatrol.com</span></div>
</section>

<section class="card permits">
  <div class="permit-box">
    <h3>CURRENT PERMITS</h3>
    <div>Guard Card : Red When Invalid</div>
    <div>Expiring Date : 22/04/2020</div>
    <div>SSN : **************9659</div>
    <h3 class="second">STATE ID</h3>
    <div class="lic">Driver License Expiry<br>Date : 02/09/2020</div>
  </div>
</section>

<section class="message msg-employee">
  <h3>EMPLOYEE SPECIAL MESSAGE</h3>
  <p><span class="q">&ldquo;</span> Sed ut perspiciatis unde omnis iste natus error<br>sit voluptatem accusantium dolore <span class="q">&rdquo;</span></p>
</section>

<section class="message msg-company">
  <h3>COMPANY SPECIAL MESSAGE</h3>
  <p><span class="q">&ldquo;</span> Sed ut perspiciatis unde omnis iste natus error<br>sit voluptatem accusantium dolore <span class="q">&rdquo;</span></p>
</section>

<section class="card calendar">
  <div class="cal">
    <div class="cal-head">
      <span class="cal-btn"><svg width="7" height="10" viewBox="0 0 7 10"><path d="M5.5 1 1.5 5l4 4" fill="none" stroke="#fff" stroke-width="1.8"/></svg></span>
      <span>SEPTEMBER</span>
      <span class="cal-btn"><svg width="7" height="10" viewBox="0 0 7 10"><path d="M1.5 1l4 4-4 4" fill="none" stroke="#fff" stroke-width="1.8"/></svg></span>
    </div>
    <div class="cal-days"><span>Mon</span><span>Tue</span><span>Wed</span><span>Thu</span><span>Fri</span><span>Sat</span><span>Sun</span></div>
    <div class="cal-grid">
      <span>1</span><span>2</span><span>3</span><span>4</span><span>5</span><span>6</span><span>7</span>
      <span>8</span><span>9</span><span>10</span><span>11</span><span>12</span><span>13</span><span>14</span>
      <span>15</span><span>16</span><span>17</span><span>18</span><span>19</span><span>20</span><span>21</span>
      <span>22</span><span>23</span><span>24</span><span>25</span><span>26</span><span>27</span><span>28</span>
      <span>29</span><span class="today">30</span><span>31</span><span class="out">1</span><span class="out">2</span><span class="out">3</span><span class="out">4</span>
    </div>
  </div>
</section>

<footer class="footer">
  <div class="foot-links"><span>HOME</span><i>|</i><span>PERSONAL LICENSES</span><i>|</i><span>FORMS/REQUESTS</span><i>|</i><span>TEAM CONTACT</span><i>|</i><span>BENEFITS</span><i>|</i><span>TRAINING</span><i>|</i><span>EQUIPMENT</span><i>|</i><span>HELP</span></div>
  <div class="copy">© 2016 . NORTHGATE PATROL | ALLRIGHTS RESERVED.</div>
  <div class="social"><span>CONNECT WITH US :</span><b></b><b></b><b></b><b></b><b></b></div>
</footer>
</body>
</html>
```